Steadfast Wiring and Comms needs a mail drop flyer design.

We need a flyer design to promote our electricians, to be delivered to homes in our surrounding area.
Contact details: Phone: 02 6237 4815 Mobile: 0471 562 938
Email: contact@steadfastwiring.com.au
Steadfast Wiring & Comms is a local family owned business servicing Canberra, Queanbeyan and surrounding regions. We provide a high quality and reliable service with a focus on safety and attention to detail for your home or business.
We can cater to all your electrical and data needs whether it be a new installation or an upgrade for your existing.
Domestic- We provide a full range of domestic electrical and data solutions for your home. Whether it is new installations or repairs and maintenance, we can advise you on the best solution to improve your property and save you money. Our tradesmen are experienced with all aspects of residential electrical installations. We pride ourselves on being reliable and customer focused.
Commercial- Professional electrical solutions for your business.
Electrical fit outs for new shops, offices and warehouses or refurbishment of existing premises.Emergency calls and after hours service
DOMESTIC SERVICES
New homes and renovations
Indoor and outdoor lighting
Security lighting
LED Lighting
Power points
USB Power points
Outdoor power points
Ovens
Cooktops
Switchboard upgrades
Safety switches
Hot water systems
Designated circuits
Ceiling fans
Ventoras
TV points
Smoke detectors
Fuse replacement
Telephone and data networking
Audio visual
Home theatre
Garage power and lighting
Energy audits
AFTER HOURS SERVICE AVAILABLE - Call: 0471 562 938
www.steadfastwiring.com.au
ACT Lic. No. 30457821 - NSW Lic. No. 914352K - ARC Lic. No. B726183

```html
<!DOCTYPE html>
<html lang="en">
<head>
<meta charset="utf-8">
<title>Steadfast Wiring &amp; Comms – Mail Drop Flyer</title>
<link href="https://fonts.googleapis.com/css2?family=Source+Sans+3:wght@400;700;800&family=Roboto+Condensed:wght@300;400&display=swap" rel="stylesheet">
<style>
  :root{
    --stage:#2a2a2a;
    --cream:#fff6de;
    --amber:#f5bd5c;
    --wave-brown:#7a5a32;
    --navy:#1c3a5a;
    --teal-logo:#1f5a6a;
    --panel-teal:#1a4a57;
    --footer-teal:#12343f;
    --night:#0b0d12;
    --deep-blue:#1d5a90;
    --gold-text:#f2b43c;
    --white:#ffffff;
    --ink:#1b1b1b;
    --pill:#fbd89c;
  }
  *{box-sizing:border-box;margin:0;padding:0}
  html,body{width:1200px;height:1069px;overflow:hidden;background:var(--stage)}
  body{position:relative;font-family:"Source Sans 3",sans-serif}

  .flyer{position:absolute;width:677px;height:525px;overflow:hidden}
  .flyer-front{left:56px;top:20px;background:linear-gradient(90deg,var(--deep-blue) 0%,#163e66 38%,var(--night) 62%)}
  .flyer-back{left:462px;top:519px;background:linear-gradient(180deg,var(--cream) 0%,#fde4ad 45%,var(--amber) 100%)}

  .header{position:absolute;left:0;top:0;width:100%;height:170px;z-index:2}
  .header svg{position:absolute;left:0;top:0}

  .brand{position:absolute;display:flex;align-items:center;gap:12px;color:var(--teal-logo);font-weight:800;line-height:1}
  .brand-mark{width:40px;height:40px;background:var(--teal-logo);border-radius:50%;flex:none}
  .brand-name{display:flex;flex-direction:column}
  .brand-name .big{font-size:44px;letter-spacing:-0.5px}
  .brand-name .small{font-size:23px;margin-top:2px;padding-left:38px}

  .front-brand{left:34px;top:34px}
  .back-brand{left:38px;top:36px}

  .after-hours{position:absolute;left:366px;top:50px;color:var(--navy);font-weight:700;font-size:17px;line-height:20px}
  .after-hours .call{font-size:21px;line-height:25px}

  .photo{position:absolute}
  .photo-phone{left:563px;top:20px;width:112px;height:102px;border-radius:10px;background:linear-gradient(160deg,#e9e9e9,#9aa3ab 60%,#e8b88c)}
  .photo-bulb{left:0;top:150px;width:310px;height:375px;background:linear-gradient(180deg,#2a6ea4 0%,#3f86a8 45%,#5a8a9a 70%,#8a7a6e 100%)}
  .photo-van{left:388px;top:20px;width:232px;height:124px;border-radius:18px 30px 6px 6px;background:linear-gradient(180deg,#c9cdd2 0%,#f2f2f2 40%,#d7dadd 100%)}

  .intro{position:absolute;left:313px;top:180px;width:345px;color:var(--white)}
  .intro-lead{font-family:"Roboto Condensed",sans-serif;font-weight:300;font-size:21px;line-height:30px;letter-spacing:-0.2px}
  .intro-body{margin-top:12px;font-size:14px;line-height:15.2px}
  .intro-services{margin-top:10px;font-family:"Roboto Condensed",sans-serif;font-weight:300;font-size:23px;white-space:nowrap;letter-spacing:-0.3px}

  .front-legal{position:absolute;left:393px;top:430px;color:var(--gold-text);font-size:13px;line-height:20px}

  .services-pill{position:absolute;left:0;top:164px;width:170px;height:28px;background:var(--pill);border-radius:0 10px 10px 0;
    color:var(--navy);font-weight:700;font-size:20px;line-height:28px;padding-left:34px}
  .services-list{position:absolute;top:207px;list-style:none;color:var(--ink);font-size:13.5px;line-height:16.9px}
  .services-list.col-a{left:34px}
  .services-list.col-b{left:221px;top:208px}
  .back-call{position:absolute;left:34px;top:418px;color:var(--navy);font-weight:700;font-size:16.5px;line-height:18px}
  .back-call .call{font-size:21px;line-height:23px}

  .info-panel{position:absolute;left:404px;top:144px;width:257px;height:326px;background:var(--panel-teal);padding:24px 10px 0 11px;color:var(--white)}
  .info-panel h2{font-size:20px;font-weight:700;line-height:20px}
  .info-panel p{font-size:13px;line-height:15.1px}
  .info-panel h2.second{margin-top:12px}

  .footer-band{position:absolute;left:0;top:470px;width:100%;height:55px;background:var(--footer-teal);color:var(--gold-text);
    font-size:13px;line-height:40px;padding-left:34px;white-space:nowrap}
</style>
</head>
<body>

<section class="flyer flyer-front" aria-label="Flyer front">
  <div class="photo photo-bulb" role="img" aria-label="Photo of a glowing light bulb floating above an open hand"></div>
  <div class="header">
    <svg width="677" height="170" viewBox="0 0 677 170">
      <defs>
        <linearGradient id="headGradFront" x1="0" y1="0" x2="0" y2="1">
          <stop offset="0" stop-color="#fff7e2"/>
          <stop offset="0.6" stop-color="#fbd48a"/>
          <stop offset="1" stop-color="#f2ae45"/>
        </linearGradient>
      </defs>
      <path d="M0 0H677V118C600 122 520 135 430 145C330 156 240 150 160 150C90 150 40 160 0 168Z" fill="url(#headGradFront)"/>
      <path d="M0 168C40 160 90 150 160 150C240 150 330 156 430 145C520 135 600 122 677 118V128C600 132 520 143 430 153C330 164 240 156 160 156C90 156 40 165 0 172Z" fill="var(--wave-brown)"/>
    </svg>
    <div class="brand front-brand">
      <span class="brand-mark"></span>
      <span class="brand-name"><span class="big">Steadfast</span><span class="small">Wiring &amp; Comms</span></span>
    </div>
    <div class="after-hours">AFTER HOURS<br>SERVICE AVAILABLE -<br><span class="call">Call: 0471 562 938</span></div>
    <div class="photo photo-phone" role="img" aria-label="Photo of a hand holding a smartphone showing the dial screen"></div>
  </div>

  <div class="intro">
    <p class="intro-lead">Steadfast Wiring &amp; Comms is a local family owned business servicing Canberra, Queanbeyan and surrounding regions.</p>
    <p class="intro-body">We provide a high quality and reliable service with a focus on safety and attention to detail for your home or business. We can cater to all your electrical and data needs whether it be a new installation or an upgrade for your existing.</p>
    <p class="intro-services">COMMERCIAL &amp; DOMESTIC SERVICES</p>
  </div>

  <div class="front-legal">www.steadfastwiring.com.au<br>ACT Lic. No. 30457821 -<br>NSW Lic. No. 914352K - ARC Lic. No. B726183</div>
</section>

<section class="flyer flyer-back" aria-label="Flyer back">
  <div class="header">
    <svg width="677" height="170" viewBox="0 0 677 170">
      <defs>
        <linearGradient id="headGradBack" x1="0" y1="0" x2="0" y2="1">
          <stop offset="0" stop-color="#fffaf0"/>
          <stop offset="0.55" stop-color="#fcd996"/>
          <stop offset="1" stop-color="#f3b24d"/>
        </linearGradient>
      </defs>
      <path d="M0 0H677V108C600 112 530 126 450 138C360 150 290 150 210 150C120 150 50 155 0 162Z" fill="url(#headGradBack)"/>
      <path d="M0 162C50 155 120 150 210 150C290 150 360 150 450 138C530 126 600 112 677 108V118C600 122 530 136 450 147C360 158 290 156 210 156C120 156 50 161 0 167Z" fill="var(--wave-brown)"/>
    </svg>
    <div class="brand back-brand">
      <span class="brand-mark"></span>
      <span class="brand-name"><span class="big">Steadfast</span><span class="small">Wiring &amp; Comms</span></span>
    </div>
  </div>
  <div class="photo photo-van" role="img" aria-label="Photo of the company's white service van with ladders on the roof rack"></div>

  <div class="services-pill">Our SERVICES</div>
  <ul class="services-list col-a">
    <li>New homes and renovations</li>
    <li>Indoor and outdoor lighting</li>
    <li>Security lighting</li>
    <li>LED Lighting</li>
    <li>Power points</li>
    <li>USB Power points</li>
    <li>Outdoor power points</li>
    <li>Ovens</li>
    <li>Cooktops</li>
    <li>Switchboard upgrades</li>
    <li>Safety switches</li>
    <li>Hot water systems</li>
  </ul>
  <ul class="services-list col-b">
    <li>Designated circuits</li>
    <li>Ceiling fans</li>
    <li>Ventoras</li>
    <li>TV points</li>
    <li>Smoke detectors</li>
    <li>Fuse replacement</li>
    <li>Telephone &amp; data networking</li>
    <li>Audio visual</li>
    <li>Home theatre</li>
    <li>Garage power &amp; lighting</li>
    <li>Energy audits</li>
  </ul>
  <div class="back-call">AFTER HOURS SERVICE AVAILABLE -<br><span class="call">Call: 0471 562 938</span></div>

  <div class="info-panel">
    <h2>Domestic</h2>
    <p>We provide a full range of domestic electrical and data solutions for your home. Whether it is new installations or repairs and maintenance, we can advise you on the best solution to improve your property and save you money.<br>Our tradesmen are experienced with all aspects of residential electrical installations. We pride ourselves on being reliable and customer focused.</p>
    <h2 class="second">Commercial</h2>
    <p>Professional electrical solutions for your business. Electrical fit outs for new shops, offices and warehouses or refurbishment of existing premises.Emergency calls and after hours service</p>
  </div>

  <div class="footer-band">www.steadfastwiring.com.au &nbsp;| &nbsp;ACT Lic. No. 30457821 - NSW Lic. No. 914352K - ARC Lic. No. B726183</div>
</section>

</body>
</html>
```